Business Card Design Project

We need a Business Card for an Mechanical Engineering firm in Singapore. The design should be Modern & Technical looking, yet eye catching.

Our company deals in Cutting Tools & Machine Accessories for the Manufacturing Industries such as Oil & Gas, Aero Space, etc... For more information on our Company, you can either email me or view our website www.valtrion.com.sg.

We are trying to revamp our image to give our consumers a fresh new perspective to our company, so we welcome all ideas.

Industry/Entity Type

Business

Requirements
Must have
• Must incorporate New Company Logo into the card as shown in Uploaded file.

```html
<!DOCTYPE html>
<html lang="en">
<head>
<meta charset="utf-8">
<title>Valtrion Tools – Business Card</title>
<link rel="stylesheet" href="https://fonts.googleapis.com/css2?family=PT+Serif:wght@400;700&display=swap">
<style>
  :root {
    --page-bg: #ecebea;
    --maroon: #7a1030;
    --maroon-deep: #5e0a26;
    --ink: #3a0f1e;
    --pink-light: #f5b8cb;
    --pink-mid: #d995ad;
    --plum: #6b2a42;
    --card-white: #ffffff;
    --text-dark: #2a1a20;
    --ghost: #e9e9e9;
  }
  * { margin: 0; padding: 0; box-sizing: border-box; }
  html, body {
    width: 1112px; height: 1200px; overflow: hidden;
    background: var(--page-bg);
    font-family: "PT Serif", Georgia, serif;
  }
  .canvas { position: relative; width: 1112px; height: 1200px; }

  .card {
    position: absolute; left: 262px; width: 588px; height: 390px;
    border-radius: 23px; overflow: hidden;
  }

  /* Front */
  .card-front {
    top: 193px;
    background: linear-gradient(180deg, var(--pink-light) 0%, #eeaec3 45%, var(--pink-mid) 68%, var(--plum) 100%);
  }
  .front-sheen {
    position: absolute; left: -60px; top: -250px; width: 760px; height: 560px;
    border-radius: 50%;
    background: linear-gradient(180deg, rgba(255,255,255,0) 40%, rgba(255,255,255,0.22) 100%);
  }
  .front-decoration {
    position: absolute; left: 0; top: 0; width: 230px; height: 230px;
    border-top-left-radius: 23px;
    background: radial-gradient(circle at 30% 30%, rgba(122,40,70,0.55) 0%, rgba(122,40,70,0.25) 50%, rgba(122,40,70,0) 72%);
  }
  .front-brand {
    position: absolute; left: 0; right: 0; top: 150px;
    display: flex; justify-content: center; align-items: center; gap: 12px;
  }
  .brand-dot { width: 20px; height: 20px; border-radius: 50%; background: var(--maroon); }
  .brand-name {
    font-weight: 700; color: var(--maroon); font-size: 40px; letter-spacing: 1px;
  }
  .front-web {
    position: absolute; left: 0; right: 0; top: 328px; text-align: center;
    font-weight: 700; font-size: 20px; letter-spacing: 1px; color: var(--ink);
  }

  /* Back */
  .card-back { top: 617px; background: var(--card-white); }
  .back-decoration {
    position: absolute; left: 225px; top: 15px; width: 340px; height: 320px;
    background: radial-gradient(ellipse at 60% 50%, var(--ghost) 0%, rgba(233,233,233,0.6) 45%, rgba(233,233,233,0) 72%);
  }
  .back-brand {
    position: absolute; left: 30px; top: 56px;
    display: flex; align-items: center; gap: 8px;
  }
  .back-brand .brand-dot { width: 13px; height: 13px; }
  .back-brand .brand-name { font-size: 25px; }
  .address {
    position: absolute; left: 57px; top: 167px;
    font-size: 13.5px; line-height: 18.5px; color: var(--text-dark);
  }
  .contacts {
    position: absolute; left: 57px; top: 255px; list-style: none;
    font-size: 13.5px; line-height: 18.5px; color: var(--text-dark);
  }
  .contacts li { display: flex; align-items: center; gap: 12px; }
  .contacts svg { width: 13px; height: 13px; flex: none; }
  .rule-thin {
    position: absolute; left: 0; right: 0; top: 355px; height: 4px; background: var(--ink);
  }
  .band {
    position: absolute; left: 0; right: 0; top: 363px; bottom: 0; background: var(--maroon-deep);
  }
</style>
</head>
<body>
<main class="canvas">

  <section class="card card-front">
    <div class="front-sheen"></div>
    <div class="front-decoration" role="img" aria-label="Large decorative brand motif in dark maroon"></div>
    <div class="front-brand">
      <span class="brand-dot"></span>
      <span class="brand-name">VALTRION TOOLS</span>
    </div>
    <p class="front-web">www.valtrion.com.sg</p>
  </section>

  <section class="card card-back">
    <div class="back-decoration" role="img" aria-label="Faint decorative brand motif in light grey"></div>
    <div class="back-brand">
      <span class="brand-dot"></span>
      <span class="brand-name">VALTRION TOOLS</span>
    </div>
    <address class="address" style="font-style:normal">
      VALTRION TOOLS PTE LTD<br>
      27 KALLANG WAY #03-12,<br>
      MERIDIAN INDUSTRIAL PARK,<br>
      SINGAPORE 349281
    </address>
    <ul class="contacts">
      <li>
        <svg viewBox="0 0 16 16" aria-hidden="true"><path fill="#7a1030" d="M4 1l3 3-1.6 2a9 9 0 0 0 4.6 4.6L12 9l3 3-2 3C7 15 1 9 1 3z"/></svg>
        65-63120457
      </li>
      <li>
        <svg viewBox="0 0 16 16" aria-hidden="true"><path fill="#7a1030" d="M3 1h7l3 3v11H3z"/><path fill="#fff" d="M5 7h6v1H5zm0 2h6v1H5zm0 2h6v1H5z"/></svg>
        65-63120458
      </li>
      <li>
        <svg viewBox="0 0 16 16" aria-hidden="true"><rect x="1" y="3" width="14" height="10" fill="none" stroke="#7a1030" stroke-width="1.2"/><path d="M1 3l7 6 7-6" fill="none" stroke="#7a1030" stroke-width="1.2"/></svg>
        INFO@VALTRION.COM.SG
      </li>
      <li>
        <svg viewBox="0 0 16 16" aria-hidden="true"><circle cx="8" cy="8" r="7" fill="#7a1030"/><path d="M1 8h14M8 1c3 3 3 11 0 14M8 1c-3 3-3 11 0 14" fill="none" stroke="#fff" stroke-width="1"/></svg>
        WWW.VALTRION.COM.SG
      </li>
    </ul>
    <div class="rule-thin"></div>
    <div class="band"></div>
  </section>

</main>
</body>
</html>
```